New For Sale Signs

We are looking for a design not too dissimilar to the attached. Looking more for tweaks than a radically new concept. The attached just isn't quite right. Looking to add a touch more grey (our secondary colour). We look forward to seeing your new designs!

Thank you so much for all of your creative input. We have now found the perfect design but very much appreciate your participation and wish you all the best. Kind regards, Rosalind Pemberly Brightwell Estate Agents

```html
<!DOCTYPE html>
<html lang="en">
<head>
<meta charset="utf-8">
<title>Brightwell Estate Agents – For Sale Sign</title>
<link rel="stylesheet" href="https://fonts.googleapis.com/css2?family=Inter:wght@300;400;500&display=swap">
<style>
  :root {
    --backdrop: #e4e4e4;
    --brand-teal: #005f6e;
    --brand-grey: #a9a9a9;
    --soft-grey: #a5b3b8;
    --white: #ffffff;
  }
  html, body {
    margin: 0;
    padding: 0;
    width: 957px;
    height: 1200px;
    overflow: hidden;
    background: var(--backdrop);
  }
  .sign {
    position: absolute;
    left: 143px;
    top: 97px;
    width: 670px;
    height: 1004px;
    background: var(--brand-teal);
    font-family: "Inter", Arial, sans-serif;
    text-align: center;
  }
  .sign > * {
    position: absolute;
    left: 0;
    right: 0;
    margin: 0;
  }
  .brand-name {
    top: 72px;
    font-size: 74px;
    font-weight: 400;
    letter-spacing: 0.07em;
    line-height: 1;
    color: var(--white);
  }
  .brand-descriptor {
    top: 174px;
    font-size: 24px;
    font-weight: 400;
    letter-spacing: 0.32em;
    line-height: 1;
    color: var(--white);
  }
  .status-frame {
    left: 53px;
    right: 55px;
    top: 299px;
    height: 126px;
    border: 7px solid var(--brand-grey);
    display: flex;
    align-items: center;
    justify-content: center;
  }
  .status-label {
    font-size: 106px;
    font-weight: 500;
    line-height: 1;
    color: var(--brand-grey);
    letter-spacing: -0.01em;
  }
  .tagline {
    top: 528px;
    font-size: 76px;
    font-weight: 300;
    letter-spacing: -0.02em;
    line-height: 1;
    color: var(--soft-grey);
  }
  .enquiry-note {
    top: 649px;
    font-size: 33px;
    font-weight: 300;
    line-height: 53px;
    color: var(--soft-grey);
  }
  .phone-number {
    top: 786px;
    font-size: 104px;
    font-weight: 300;
    line-height: 1;
    color: var(--white);
  }
  .web-address {
    top: 932px;
    font-size: 36px;
    font-weight: 300;
    line-height: 1;
    color: var(--soft-grey);
  }
</style>
</head>
<body>
  <main class="sign">
    <p class="brand-name">BRIGHTWELL</p>
    <p class="brand-descriptor">ESTATE AGENTS</p>
    <div class="status-frame"><span class="status-label">FOR SALE</span></div>
    <p class="tagline">Homes.Handled.</p>
    <p class="enquiry-note">For further information regarding<br>this property please call</p>
    <p class="phone-number">4310 5262</p>
    <p class="web-address">brightwellestateagents.com.au</p>
  </main>
</body>
</html>
```